Kestrel Signs Facebook Banner Design

Design a facebook banner for a sign company. I would like to have a modern approach to it.

Product Offering:
Signs
Banners
Decals
Commercial Wraps

```html
<!DOCTYPE html>
<html lang="en">
<head>
<meta charset="UTF-8">
<title>Kestrel Signs – Facebook Banner</title>
<link rel="stylesheet" href="https://fonts.googleapis.com/css2?family=Poppins:ital,wght@0,400;0,700;0,800;1,600&display=swap">
<style>
  :root {
    --stage: #404040;
    --brand-red: #e8343a;
    --accent-orange: #ffa04a;
    --ink: #1f1f1f;
    --white: #ffffff;
    --band-light: #fdf3f1;
    --band-pink: #fbe4e0;
    --swatch-tint: #f26a6e;
    --bottle-blue: #1f5fb8;
    --bottle-deep: #173c7d;
    --mug-white: #f1f1f1;
  }
  * { margin: 0; padding: 0; box-sizing: border-box; }
  html, body {
    width: 1200px;
    height: 630px;
    overflow: hidden;
    background: var(--stage);
    font-family: "Poppins", sans-serif;
  }
  .banner {
    position: absolute;
    left: 0;
    top: 84px;
    width: 1200px;
    height: 463px;
    background: var(--brand-red);
    overflow: hidden;
  }
  .banner-shapes {
    position: absolute;
    inset: 0;
  }
  .headline {
    position: absolute;
    left: 68px;
    top: 56px;
    font-size: 43px;
    line-height: 66px;
    letter-spacing: 0.5px;
  }
  .headline-light {
    display: block;
    font-weight: 400;
    color: var(--white);
  }
  .headline-bold {
    display: block;
    font-weight: 800;
    color: var(--ink);
    letter-spacing: -0.5px;
  }
  .services {
    position: absolute;
    left: 68px;
    top: 212px;
    display: flex;
    gap: 16px;
    list-style: none;
    font-style: italic;
    font-weight: 600;
    font-size: 19px;
    color: var(--white);
  }
  .services li {
    display: flex;
    align-items: center;
    gap: 5px;
  }
  .services li::before {
    content: "";
    width: 9px;
    height: 9px;
    border-radius: 50%;
    background: var(--ink);
  }
  .cta {
    position: absolute;
    left: 68px;
    top: 279px;
    width: 362px;
    height: 52px;
    border-radius: 26px;
    background: var(--accent-orange);
    color: var(--white);
    font-weight: 800;
    font-size: 27px;
    display: flex;
    align-items: center;
    justify-content: center;
    letter-spacing: 0.3px;
  }
  .brand-name {
    position: absolute;
    left: 850px;
    top: 330px;
    width: 300px;
    text-align: center;
    font-weight: 800;
    font-size: 38px;
    line-height: 42px;
    color: var(--brand-red);
    letter-spacing: 1px;
  }
</style>
</head>
<body>
  <section class="banner">
    <svg class="banner-shapes" width="1200" height="463" viewBox="0 0 1200 463">
      <defs>
        <linearGradient id="band-fill" x1="0" y1="0" x2="1" y2="0">
          <stop offset="0" stop-color="var(--band-pink)"/>
          <stop offset="1" stop-color="var(--band-light)"/>
        </linearGradient>
        <linearGradient id="bottle-fill" x1="0" y1="0" x2="0" y2="1">
          <stop offset="0" stop-color="var(--bottle-blue)"/>
          <stop offset="1" stop-color="var(--bottle-deep)"/>
        </linearGradient>
      </defs>
      <polygon class="light-band" points="336,463 1200,281 1200,463" fill="url(#band-fill)"/>
      <rect class="swatch-fan" role="img" aria-label="Illustration of a fanned colour swatch book"
            x="0" y="232" width="318" height="231" rx="10" fill="var(--swatch-tint)" opacity="0.45"/>
      <rect class="dot-pattern" role="img" aria-label="Decorative dot pattern"
            x="1140" y="2" width="185" height="100" fill="var(--white)" opacity="0.12" transform="translate(-150 0)"/>
      <rect class="accent-burst" role="img" aria-label="Decorative orange star shape"
            x="705" y="195" width="80" height="60" rx="12" fill="var(--accent-orange)" opacity="0.85"/>
      <rect class="accent-sparkle" role="img" aria-label="Decorative orange sparkle"
            x="648" y="405" width="70" height="58" rx="12" fill="var(--accent-orange)" opacity="0.8"/>
      <rect class="product-bottle" role="img" aria-label="Photo of a blue branded water bottle"
            x="505" y="262" width="404" height="112" rx="40" fill="url(#bottle-fill)"
            transform="rotate(-14 707 318)"/>
      <rect class="product-mug" role="img" aria-label="Photo of a white branded coffee mug"
            x="932" y="89" width="208" height="187" rx="26" fill="var(--mug-white)"/>
    </svg>

    <h1 class="headline">
      <span class="headline-light">ELEVATE YOUR BRAND WITH</span>
      <span class="headline-bold">STUNNING SIGNAGE</span>
    </h1>

    <ul class="services">
      <li>SIGNS</li>
      <li>BANNERS</li>
      <li>DECALS</li>
      <li>COMMERCIAL WRAPS</li>
    </ul>

    <div class="cta">CONTACT US TODAY</div>

    <div class="brand-name">KESTREL<br>SIGNS</div>
  </section>
</body>
</html>
```